Industrial Services company needs a business card design

We provide industrial maintenance services including sandblasting, painting, pressure washing, storage tank rehabilitation, and welding. I would like an industrial design that's eye catching. I would like the back-side of the card to list our services.

Industry/Entity Type

Construction

Contact Information for Business Card

address: 418 Hartwell Lane, York, PA 17405
Phone: 410-637-4815
email: corvethinc@mailbrook.net
Daniel Verhoeven, President
www.corvethcoating.net

Logo Text

Corveth Industrial Services

Font styles to use
Sans Serif

Colors
000000
229ed3
0692cd
ffffff

Requirements
Must have
• Easy to read
• our services listed/included on back of card
• eye catching color combinations
Nice to have
• Water storage tank image

```html
<!DOCTYPE html>
<html lang="en">
<head>
<meta charset="utf-8">
<title>Corveth Industrial Services – Business Card</title>
<link href="https://fonts.googleapis.com/css2?family=Lato:wght@400;700&family=Montserrat:wght@500;600&display=swap" rel="stylesheet">
<style>
  :root {
    --backdrop: #3b3430;
    --card: #0b0b0b;
    --ink: #ffffff;
    --ink-soft: #d9d9d9;
    --silver: #c9c9c9;
    --blue: #229ed3;
    --blue-deep: #0692cd;
    --rule: #5a5a5a;
  }
  * { box-sizing: border-box; margin: 0; padding: 0; }
  html, body { width: 1200px; height: 900px; overflow: hidden; }
  body {
    background: var(--backdrop);
    font-family: "Lato", sans-serif;
    position: relative;
  }
  .card {
    position: absolute;
    top: 300px;
    width: 525px;
    height: 300px;
    background: var(--card);
    border-radius: 4px;
    overflow: hidden;
  }
  .card--contact { left: 50px; }
  .card--services { left: 625px; }

  /* contact side */
  .brand-block {
    position: absolute;
    left: 0; top: 0;
    width: 232px; height: 100%;
    display: flex;
    align-items: center;
    justify-content: center;
    gap: 12px;
  }
  .brand-dot {
    width: 22px; height: 22px;
    border-radius: 50%;
    background: var(--blue-deep);
  }
  .brand-name {
    font-family: "Montserrat", sans-serif;
    font-weight: 600;
    font-size: 24px;
    letter-spacing: 2px;
    color: var(--blue);
  }
  .divider {
    position: absolute;
    left: 232px; top: 0;
    width: 1px; height: 160px;
    background: var(--rule);
  }
  .contact {
    position: absolute;
    left: 255px; top: 48px;
    color: var(--ink);
  }
  .contact__name {
    font-size: 19px;
    font-weight: 400;
    letter-spacing: .5px;
    color: var(--blue);
    text-transform: uppercase;
  }
  .contact__role { font-size: 15px; margin-bottom: 12px; }
  .contact__address { font-size: 15px; line-height: 1.25; margin-bottom: 12px; }
  .contact__line {
    display: flex; align-items: center; gap: 8px;
    font-size: 15px; line-height: 1.35;
  }
  .contact__line svg { width: 11px; height: 11px; fill: var(--blue); flex: none; }

  /* services side */
  .services-side {
    position: absolute; inset: 0;
    display: flex; flex-direction: column; align-items: center;
    padding-top: 62px;
  }
  .company-name {
    font-family: "Montserrat", sans-serif;
    font-weight: 600;
    font-size: 28px;
    letter-spacing: 3px;
    color: var(--silver);
    text-transform: uppercase;
    text-align: center;
    line-height: 1.25;
  }
  .services-rule {
    width: 400px; height: 1px;
    background: var(--silver);
    margin: 24px 0 14px;
  }
  .services-rule--bottom { margin: 14px 0 0; }
  .services-list {
    color: var(--ink-soft);
    font-size: 12.5px;
    letter-spacing: .4px;
    text-transform: uppercase;
    text-align: center;
    line-height: 1.55;
  }
</style>
</head>
<body>

  <section class="card card--contact" aria-label="Business card, contact side">
    <div class="brand-block">
      <span class="brand-dot"></span>
      <span class="brand-name">CORVETH</span>
    </div>
    <div class="divider"></div>
    <div class="contact">
      <p class="contact__name">Daniel Verhoeven</p>
      <p class="contact__role">President</p>
      <p class="contact__address">418 Hartwell Lane<br>York, PA 17405</p>
      <p class="contact__line">
        <svg viewBox="0 0 16 16" aria-hidden="true"><path d="M3 1l3 3-1.5 2a9 9 0 005 5l2-1.5 3 3-2 2C6 14 2 10 1 3z"/></svg>
        410-637-4815
      </p>
      <p class="contact__line">
        <svg viewBox="0 0 16 16" aria-hidden="true"><path d="M1 3h14v10H1z M1 3l7 6 7-6" stroke="#0b0b0b" stroke-width="1.2"/></svg>
        corvethinc@mailbrook.net
      </p>
      <p class="contact__line">
        <svg viewBox="0 0 16 16" aria-hidden="true"><circle cx="8" cy="8" r="7"/></svg>
        www.corvethcoating.net
      </p>
    </div>
  </section>

  <section class="card card--services" aria-label="Business card, services side">
    <div class="services-side">
      <h1 class="company-name">Corveth<br>Industrial Services</h1>
      <div class="services-rule"></div>
      <p class="services-list">
        Sandblasting | Industrial Painting | Pressure Washing | Welding<br>
        Storage Tank Inspection, Maintenance, Rehabilitation<br>
        Repair, &amp; Demolition
      </p>
      <div class="services-rule services-rule--bottom"></div>
    </div>
  </section>

</body>
</html>
```